Bref créative
Marisela Quarn Insurance biz card
biz card and stationary
Bright & Fun-filled
Marisela Quarn
Independent Agent
Charlotte, NC
mquarn@brookvantnet.example
please use the headshot and the logo that are attached.
please use the content of the back of the card we have included.
headshot
logo
card back

```html
<!DOCTYPE html>
<html lang="en">
<head>
<meta charset="utf-8">
<title>Marisela Quarn Insurance – Business Card</title>
<link href="https://fonts.googleapis.com/css2?family=Cinzel:wght@600&family=PT+Serif:wght@400;700&display=swap" rel="stylesheet">
<style>
  :root{
    --bg:#e9ebee;
    --card-white:#ffffff;
    --blue-deep:#0d5aa8;
    --blue-mid:#2a86d4;
    --blue-light:#7cc3f0;
    --brand-blue:#1f63b0;
    --ink-grey:#4a4f55;
    --accent-orange:#f0a23a;
    --text-white:#ffffff;
  }
  *{box-sizing:border-box;margin:0;padding:0}
  html,body{width:1200px;height:901px;overflow:hidden;background:var(--bg)}
  .stage{width:1200px;height:901px;display:flex;align-items:center;justify-content:center;gap:40px}
  .card{width:540px;height:310px;border-radius:14px;position:relative;overflow:hidden;
        box-shadow:0 6px 18px rgba(0,0,0,.18)}
  /* back */
  .card-back{background:linear-gradient(160deg,var(--blue-light) 0%,var(--blue-mid) 45%,var(--blue-deep) 100%);
             font-family:"PT Serif",serif;color:var(--text-white)}
  .card-back .glow{position:absolute;right:40px;top:-20px;width:260px;height:200px;border-radius:50%;
             background:radial-gradient(circle,rgba(255,255,255,.45),rgba(255,255,255,0) 70%)}
  .services{position:absolute;left:34px;top:70px}
  .services h2{font-size:16px;font-weight:700;margin-bottom:10px}
  .services ul{list-style:none}
  .services li{font-size:15px;line-height:24px;padding-left:18px;position:relative}
  .services li::before{content:"";position:absolute;left:2px;top:9px;width:6px;height:6px;border-radius:50%;background:var(--text-white)}
  /* front */
  .card-front{background:var(--card-white);font-family:"PT Serif",serif}
  .brand{position:absolute;top:34px;left:0;right:0;text-align:center}
  .brand-dot{width:54px;height:54px;border-radius:50%;background:var(--accent-orange);margin:0 auto 10px}
  .brand-name{font-family:"Cinzel",serif;font-weight:600;color:var(--brand-blue);font-size:30px;line-height:1;letter-spacing:1px}
  .brand-sub{font-family:"Cinzel",serif;font-weight:600;color:var(--brand-blue);font-size:17px;letter-spacing:2px;margin-top:4px}
  .details{position:absolute;top:178px;left:0;right:0;display:flex;justify-content:center;align-items:center;gap:22px}
  .agent .name{color:var(--brand-blue);font-weight:700;font-size:17px}
  .agent .role{color:var(--ink-grey);font-size:13px;margin-top:2px}
  .divider{width:1px;height:42px;background:#b9c2cc}
  .contact p{display:flex;align-items:center;gap:8px;font-size:12px;color:var(--ink-grey);line-height:20px}
  .contact svg{width:12px;height:12px;fill:var(--brand-blue)}
  .front-band{position:absolute;left:0;right:0;bottom:0;height:40px;
              background:linear-gradient(180deg,var(--blue-light),var(--blue-mid));border-top:3px solid var(--accent-orange)}
</style>
</head>
<body>
<main class="stage">
  <section class="card card-back">
    <div class="glow"></div>
    <div class="services">
      <h2>I can also help you with......</h2>
      <ul>
        <li>Medicare Advantage Plans</li>
        <li>Long-Term Care Insurance</li>
        <li>Fixed Annuities</li>
        <li>Life Insurance</li>
        <li>Medicare Supplement Insurance</li>
        <li>Individual Major Medical</li>
        <li>Dental Insurance</li>
      </ul>
    </div>
  </section>

  <section class="card card-front">
    <div class="brand">
      <div class="brand-dot"></div>
      <div class="brand-name">MARISELA QUARN</div>
      <div class="brand-sub">INSURANCE CONSULTANT</div>
    </div>
    <div class="details">
      <div class="agent">
        <p class="name">Marisela Quarn</p>
        <p class="role">Independent Agent</p>
      </div>
      <div class="divider"></div>
      <div class="contact">
        <p><svg viewBox="0 0 24 24"><path d="M6.6 10.8a15 15 0 006.6 6.6l2.2-2.2a1 1 0 011-.25 11.4 11.4 0 003.6.57 1 1 0 011 1V20a1 1 0 01-1 1A17 17 0 013 4a1 1 0 011-1h3.5a1 1 0 011 1c0 1.25.2 2.45.57 3.57a1 1 0 01-.25 1z"/></svg>555-014-2287</p>
        <p><svg viewBox="0 0 24 24"><path d="M2 5h20v14H2zM4 7v.5l8 5 8-5V7l-8 5z"/></svg>mquarn@brookvantnet.example</p>
      </div>
    </div>
    <div class="front-band"></div>
  </section>
</main>
</body>
</html>
```